Add words, element to an already make product design

Hi guys,
I m already have the design (attached) which is a wet tissue product. The front main side (about 14cm x 7 cm) is the waves and the brand name Zelfo. However, in this main side, it should contain more words, which are "Khan uot" (mean wet wipe), and the words "Mat lanh" (mean cooling) and "Tinh khiet" (mean purity). "Khan uot" to indicate function of the product, while Mat lanh and Tinh khiet are just marketing term to add.
So yes, the task is quite simple, but I think the key is to choose an appropriate font, color and the location you decide where it should be. You can add any element you want, as long as it look good overall, and those words above, are required to have. More in the attached are few rival from our market, as some example.
Thank you, and wait your idea.

Hi guys, Just to tell you that the main front design will not change. So the waves and the brand name still keep the same. Just adding more words or elements to it. Thank you guys.

```html
<!DOCTYPE html>
<html lang="vi">
<head>
<meta charset="utf-8">
<title>Zelfo Khan Uot – front panel</title>
<link rel="stylesheet" href="https://fonts.googleapis.com/css2?family=Pacifico&family=Montserrat:wght@500;600&display=swap">
<style>
  :root {
    --page-bg: #ffffff;
    --navy-deep: #061945;
    --navy: #0b2a6e;
    --blue-mid: #1f64b8;
    --blue-light: #8cc7ec;
    --aqua-pale: #e4f4fc;
    --white: #ffffff;
    --pill-bg: #10418f;
  }
  * { box-sizing: border-box; margin: 0; padding: 0; }
  html, body { width: 882px; height: 1200px; overflow: hidden; background: var(--page-bg); }
  .canvas { position: relative; width: 882px; height: 1200px; }
  .front-panel {
    position: absolute; left: 23px; top: 435px;
    width: 836px; height: 330px; overflow: hidden;
  }
  .front-panel svg { position: absolute; inset: 0; }
  .claims {
    position: absolute; left: 12px; top: 52px;
    display: flex; flex-direction: column; gap: 40px;
  }
  .claim {
    display: flex; align-items: center; gap: 8px;
    width: 116px; height: 34px; padding: 0 10px;
    border-radius: 17px; background: var(--pill-bg);
    color: var(--white);
    font-family: "Montserrat", sans-serif; font-weight: 600; font-size: 14px;
    white-space: nowrap;
  }
  .claim-dot { width: 12px; height: 12px; border-radius: 50%; background: var(--blue-light); flex: none; }
  .brand-block {
    position: absolute; left: 190px; top: 40px; width: 400px;
    text-align: center; color: var(--white);
  }
  .brand-name { font-family: "Pacifico", cursive; font-size: 100px; line-height: 150px; }
  .product-type {
    font-family: "Montserrat", sans-serif; font-weight: 500;
    font-size: 20px; letter-spacing: 3px; margin-top: 6px;
  }
</style>
</head>
<body>
<div class="canvas">
  <section class="front-panel">
    <svg width="836" height="330" viewBox="0 0 836 330" xmlns="http://www.w3.org/2000/svg">
      <defs>
        <linearGradient id="waterArt" x1="0" y1="0" x2="0" y2="1">
          <stop offset="0" stop-color="#e4f4fc"/>
          <stop offset="0.3" stop-color="#a6d6f2"/>
          <stop offset="0.6" stop-color="#2f78c6"/>
          <stop offset="1" stop-color="#0b3a8a"/>
        </linearGradient>
        <radialGradient id="splashArt" cx="0.55" cy="0.55" r="0.55">
          <stop offset="0" stop-color="#f4fafe"/>
          <stop offset="0.45" stop-color="#c6e6f8" stop-opacity="0.8"/>
          <stop offset="1" stop-color="#8cc7ec" stop-opacity="0"/>
        </radialGradient>
        <linearGradient id="leftBand" x1="0" y1="0" x2="1" y2="0">
          <stop offset="0" stop-color="#061945"/>
          <stop offset="1" stop-color="#0c2f7a"/>
        </linearGradient>
      </defs>
      <rect class="water-illustration" role="img" aria-label="Water waves with bubbles" x="0" y="0" width="836" height="330" fill="url(#waterArt)"/>
      <rect class="splash-illustration" role="img" aria-label="Water splash with an opened wet wipe pack" x="520" y="0" width="316" height="330" fill="url(#splashArt)"/>
      <rect class="claim-band" width="140" height="330" fill="url(#leftBand)"/>
      <circle class="brand-circle" cx="385" cy="210" r="175" fill="#0b2a6e"/>
    </svg>
    <div class="claims">
      <div class="claim"><span class="claim-dot"></span>Tinh khiet</div>
      <div class="claim"><span class="claim-dot"></span>Mat lanh</div>
    </div>
    <div class="brand-block">
      <div class="brand-name">Zelfo</div>
      <div class="product-type">KHAN UOT</div>
    </div>
  </section>
</div>
</body>
</html>
```